Nursing Concepts Diagram

We are looking to make a diagram to represent the Conceptual Framework of our nursing program (college). The frame work is based on three parts:

I. Nursing Process

II. Core Concepts
a. Clinical Competence
b. Critical Thinking
c. Moral/Ethical Principles
d. Growth Mindset
e. Caring/Compassion
f. Cultural Competence
g. Effective Communication
h. Life-long Learning

III. Brennick's Hierarchy of Needs

I have attached two sketches to give you a sense of how I think this could work.

Please also consider the following:

-Brennick's Hierarchy of Needs is always represented in the shape of a pyramid so I think the other two components (Nursing Process and Core Concepts) should complement that.

Target Market(s)

Healthcare Professionals, Nursing Educators

Font styles to use
Sans Serif

Colors

Designer to choose colors to be used in the design.

Requirements
Must have
• We would like the diagram to include a legend somewhere on the paper that outlines the parts of each component like demonstrated in the attached table
• All the small parts of the Nursing Process and Brennick's Hierarchy of Needs don't need to be listed out in the diagram because it may look too wordy, but the eight parts that make up the core concepts should all be listed
• The Nursing Process and Brennick's Hierachy of needs should both border each of the 8 core concepts so that it can show a relation.

```html
<!DOCTYPE html>
<html lang="en">
<head>
<meta charset="utf-8">
<title>Nursing Program Conceptual Framework</title>
<link rel="stylesheet" href="https://fonts.googleapis.com/css2?family=Comfortaa:wght@700&family=Montserrat:wght@600;700&family=Oswald:wght@500&family=Roboto:wght@400&display=swap">
<style>
  :root {
    --bg: #f6f6f8;
    --ink: #333333;
    --title-teal: #0f6b80;
    --title-red: #e8202a;
    --ring-olive: #c7c23a;
    --ring-green: #22770e;
    --ring-red: #b5090f;
    --ring-blue: #086a8a;
    --ring-orange: #f26a21;
    --ring-black: #000000;
    --ring-teal: #6cc0b0;
    --ring-gray: #b3b3b3;
    --disc-gray: #b3b3b5;
    --pyr-red: #ec1c24;
    --pyr-blue: #0a6c8c;
    --pyr-olive: #c9c33a;
    --pyr-green: #0aa64c;
    --pyr-dark: #444444;
  }
  html, body {
    margin: 0;
    padding: 0;
    overflow: hidden;
    background: var(--bg);
  }
  .canvas {
    position: relative;
    width: 1200px;
    height: 927px;
    background: var(--bg);
    overflow: hidden;
  }
  .framework {
    position: absolute;
    left: 0;
    top: 0;
  }
  .big-word {
    font-family: "Comfortaa", sans-serif;
    font-weight: 700;
    font-size: 92px;
    letter-spacing: 8px;
    fill: var(--title-teal);
  }
  .arc-title {
    font-family: "Comfortaa", sans-serif;
    font-weight: 700;
    font-size: 31px;
    letter-spacing: 1px;
    fill: var(--title-red);
  }
  .concept-label {
    font-family: "Montserrat", sans-serif;
    font-weight: 700;
    font-size: 16px;
    letter-spacing: 0.5px;
    fill: #ffffff;
  }
  .need-label {
    font-family: "Montserrat", sans-serif;
    font-weight: 600;
    font-size: 14.5px;
    letter-spacing: 0.4px;
    fill: #ffffff;
  }
  .legend {
    position: absolute;
    top: 722px;
    margin: 0;
  }
  .legend h2 {
    margin: 0 0 18px;
    font-family: "Oswald", sans-serif;
    font-weight: 500;
    font-size: 17px;
    letter-spacing: 0.2px;
    color: var(--ink);
  }
  .legend ul {
    list-style: none;
    margin: 0;
    padding: 0;
  }
  .legend li {
    position: relative;
    height: 24px;
    padding-left: 18px;
    font-family: "Roboto", sans-serif;
    font-size: 11px;
    line-height: 12px;
    color: var(--ink);
  }
  .legend li::before {
    content: "";
    position: absolute;
    left: 0;
    top: 1px;
    width: 10px;
    height: 10px;
    border-radius: 50%;
    background: var(--ink);
  }
  .legend li::after {
    content: "";
    position: absolute;
    left: 2.5px;
    top: 4px;
    width: 3px;
    height: 3px;
    border-top: 1.3px solid #fff;
    border-right: 1.3px solid #fff;
    transform: rotate(45deg);
  }
  .legend-process { left: 27px; }
  .legend-concepts { left: 340px; }
  .legend-concepts .columns { display: flex; gap: 0; }
  .legend-concepts .columns ul { width: 222px; }
  .legend-needs { left: 849px; }
</style>
</head>
<body>
<div class="canvas">
  <svg class="framework" width="1200" height="720" viewBox="0 0 1200 720" aria-label="Conceptual framework diagram">
    <defs>
      <!-- clockwise arcs centred on angle 0 -->
      <path id="cw-266" d="M245.8,-101.8 A266 266 0 0 1 245.8,101.8"/>
      <path id="cw-288" d="M266.1,-110.2 A288 288 0 0 1 266.1,110.2"/>
      <!-- counter-clockwise arcs centred on angle 0 -->
      <path id="ccw-278" d="M256.8,106.4 A278 278 0 0 0 256.8,-106.4"/>
      <path id="ccw-300" d="M277.2,114.8 A300 300 0 0 0 277.2,-114.8"/>
      <path id="word-left" d="M114.6,-314.8 A335 335 0 0 1 114.6,314.8"/>
      <path id="word-right" d="M114.6,-308.2 A328 328 0 0 1 114.6,308.2"/>
      <path id="needs-arc" d="M-24.1,-196.5 A198 198 0 1 1 -24.1,196.5"/>
    </defs>

    <!-- outer ring of core concepts -->
    <g class="concept-ring">
      <path fill="var(--ring-green)"  d="M600,46 A322 322 0 0 1 827.7,140.3 L771.1,196.9 A242 242 0 0 0 600,126 Z"/>
      <path fill="var(--ring-red)"    d="M827.7,140.3 A322 322 0 0 1 922,368 L842,368 A242 242 0 0 0 771.1,196.9 Z"/>
      <path fill="var(--ring-blue)"   d="M922,368 A322 322 0 0 1 827.7,595.7 L771.1,539.1 A242 242 0 0 0 842,368 Z"/>
      <path fill="var(--ring-orange)" d="M827.7,595.7 A322 322 0 0 1 600,690 L600,610 A242 242 0 0 0 771.1,539.1 Z"/>
      <path fill="var(--ring-black)"  d="M600,690 A322 322 0 0 1 372.3,595.7 L428.9,539.1 A242 242 0 0 0 600,610 Z"/>
      <path fill="var(--ring-teal)"   d="M372.3,595.7 A322 322 0 0 1 278,368 L358,368 A242 242 0 0 0 428.9,539.1 Z"/>
      <path fill="var(--ring-gray)"   d="M278,368 A322 322 0 0 1 372.3,140.3 L428.9,196.9 A242 242 0 0 0 358,368 Z"/>
      <path fill="var(--ring-olive)"  d="M372.3,140.3 A322 322 0 0 1 600,46 L600,126 A242 242 0 0 0 428.9,196.9 Z"/>
      <g transform="translate(600 368)" stroke="var(--bg)" stroke-width="12">
        <line x1="241" y1="0" x2="332" y2="0"/>
        <line x1="241" y1="0" x2="332" y2="0" transform="rotate(45)"/>
        <line x1="241" y1="0" x2="332" y2="0" transform="rotate(90)"/>
        <line x1="241" y1="0" x2="332" y2="0" transform="rotate(135)"/>
        <line x1="241" y1="0" x2="332" y2="0" transform="rotate(180)"/>
        <line x1="241" y1="0" x2="332" y2="0" transform="rotate(225)"/>
        <line x1="241" y1="0" x2="332" y2="0" transform="rotate(270)"/>
        <line x1="241" y1="0" x2="332" y2="0" transform="rotate(315)"/>
      </g>
    </g>

    <!-- concept labels -->
    <g class="concept-labels" text-anchor="middle">
      <g transform="translate(600 368) rotate(-67.5)">
        <text class="concept-label"><textPath href="#cw-288" startOffset="50%">CULTURAL</textPath></text>
        <text class="concept-label"><textPath href="#cw-266" startOffset="50%">COMPETENCE</textPath></text>
      </g>
      <g transform="translate(600 368) rotate(-22.5)">
        <text class="concept-label"><textPath href="#cw-288" startOffset="50%">CLINICAL</textPath></text>
        <text class="concept-label"><textPath href="#cw-266" startOffset="50%">COMPETENCE</textPath></text>
      </g>
      <g transform="translate(600 368) rotate(22.5)">
        <text class="concept-label"><textPath href="#ccw-278" startOffset="50%">CRITICAL</textPath></text>
        <text class="concept-label"><textPath href="#ccw-300" startOffset="50%">THINKING</textPath></text>
      </g>
      <g transform="translate(600 368) rotate(67.5)">
        <text class="concept-label"><textPath href="#ccw-278" startOffset="50%">MORAL/ETHICAL</textPath></text>
        <text class="concept-label"><textPath href="#ccw-300" startOffset="50%">PRINCIPLES</textPath></text>
      </g>
      <g transform="translate(600 368) rotate(112.5)">
        <text class="concept-label"><textPath href="#ccw-278" startOffset="50%">EFFECTIVE</textPath></text>
        <text class="concept-label"><textPath href="#ccw-300" startOffset="50%">COMMUNICATION</textPath></text>
      </g>
      <g transform="translate(600 368) rotate(157.5)">
        <text class="concept-label"><textPath href="#ccw-278" startOffset="50%">GROWTH</textPath></text>
        <text class="concept-label"><textPath href="#ccw-300" startOffset="50%">MINDSET</textPath></text>
      </g>
      <g transform="translate(600 368) rotate(202.5)">
        <text class="concept-label"><textPath href="#cw-288" startOffset="50%">CARING/</textPath></text>
        <text class="concept-label"><textPath href="#cw-266" startOffset="50%">COMPASSION</textPath></text>
      </g>
      <g transform="translate(600 368) rotate(247.5)">
        <text class="concept-label"><textPath href="#cw-288" startOffset="50%">LIFE-LONG</textPath></text>
        <text class="concept-label"><textPath href="#cw-266" startOffset="50%">LEARNING</textPath></text>
      </g>
    </g>

    <!-- nursing process title -->
    <g text-anchor="middle">
      <g transform="translate(600 368) rotate(192)">
        <text class="big-word"><textPath href="#word-left" startOffset="50%">NURSING</textPath></text>
      </g>
      <g transform="translate(600 368) rotate(-1)">
        <text class="big-word"><textPath href="#word-right" startOffset="50%">PROCESS</textPath></text>
      </g>
    </g>

    <!-- hierarchy of needs -->
    <circle cx="600" cy="368" r="242" fill="#ffffff"/>
    <circle cx="600" cy="368" r="180" fill="var(--disc-gray)"/>
    <g transform="translate(600 368) rotate(-90)" text-anchor="middle">
      <text class="arc-title"><textPath href="#needs-arc" startOffset="50%">BRENNICK'S HIERARCHY OF NEEDS</textPath></text>
    </g>

    <g class="needs-pyramid">
      <polygon fill="var(--pyr-red)"   points="600,185 662.1,288 537.9,288"/>
      <polygon fill="var(--pyr-blue)"  points="536.1,291 663.9,291 692.9,339 507.1,339"/>
      <polygon fill="var(--pyr-olive)" points="505.3,342 694.7,342 723,389 477,389"/>
      <polygon fill="var(--pyr-green)" points="475.2,392 724.8,392 756.2,444 443.8,444"/>
      <polygon fill="var(--pyr-dark)"  points="442,447 758,447 790,500 410,500"/>
      <g text-anchor="middle">
        <text class="need-label" x="600" y="265">ESTEEM</text>
        <text class="need-label" x="600" y="320">SAFETY NEEDS</text>
        <text class="need-label" x="600" y="370">SELF-ACTUALIZATION</text>
        <text class="need-label" x="600" y="423">LOVE AND BELONGING</text>
        <text class="need-label" x="600" y="478">PHYSIOLOGICAL NEEDS</text>
      </g>
    </g>
  </svg>

  <section class="legend legend-process">
    <h2>NURSING PROCESS</h2>
    <ul>
      <li>Assessment</li>
      <li>Nursing Diagnosis</li>
      <li>Planning</li>
      <li>Intervention</li>
      <li>Evaluation</li>
    </ul>
  </section>

  <section class="legend legend-concepts">
    <h2>CORE CONCEPTS</h2>
    <div class="columns">
      <ul>
        <li>Clinical Competence</li>
        <li>Critical Thinking</li>
        <li>Moral/Ethical Principles</li>
        <li>Growth Mindset</li>
        <li>Caring/Compassion</li>
      </ul>
      <ul>
        <li>Cultural Competence</li>
        <li>Effective Communication</li>
        <li>Life-long Learning</li>
      </ul>
    </div>
  </section>

  <section class="legend legend-needs">
    <h2>BRENNICK'S HIERARCHY OF NEEDS</h2>
    <ul>
      <li>Self-actualization</li>
      <li>Esteem</li>
      <li>Love and Belonging</li>
      <li>Safety Needs</li>
      <li>Physiological Needs</li>
    </ul>
  </section>
</div>
</body>
</html>
```